Büroausstattung Steuerberater
Alles prima. Frau Wendtke arbeitet äußerst professionell und wird von uns auch zukünftig für anstehende Arbeiten beauftragt!
Zielgruppe
Typisch Steuerberater: Vom jungen Existenzgründer bis zum Geschäftsführer eines großen Unternehmens.
Mit anderen Worten: Nicht verspielt, aber auch nicht zu bieder.
Aufgabenstellung
Wir benötigen:
-Allg. Briefpapier
-Rechnungsvorlage (mit einfacher Excel-Addition)
-Faxvorlage
-Visitenkarten
-Memo Block (DIN A4 - kariert)
Wichtig:
Wir benötigen nicht nur einen Designvorschlag, sondern fertige Word bzw. Excel Dokumente, mit denen wir direkt arbeiten bzw. diese ausdrucken können!
Da wir bereits ein Logo haben, ist die Kreierung eines Logos nicht erforderlich.

```html
<!DOCTYPE html>
<html lang="de">
<head>
<meta charset="utf-8">
<title>Geschäftsausstattung Steuerberater Holger Varnbeck</title>
<link rel="stylesheet" href="https://fonts.googleapis.com/css2?family=Open+Sans:wght@400;600;700&display=swap">
<style>
  :root {
    --brand-blue: #1f5fa8;
    --ink: #1c1c1c;
    --tab-grey: #a7a8aa;
    --stage-outer: #d2d2d2;
    --stage-light: #f4f4f4;
    --stage-dark: #cfcfcf;
    --paper: #ffffff;
    --caption: #6d6d6d;
  }
  * { box-sizing: border-box; margin: 0; padding: 0; }
  html, body { width: 1200px; height: 1200px; overflow: hidden; }
  body {
    background: var(--stage-outer);
    font-family: "Open Sans", Arial, sans-serif;
    color: var(--ink);
  }
  .stage {
    position: absolute; left: 15px; top: 15px; width: 1170px; height: 1170px;
    background: radial-gradient(circle at 50% 40%, var(--stage-light) 0%, #e6e6e6 55%, var(--stage-dark) 100%);
  }
  .sheet {
    position: absolute; background: var(--paper);
    box-shadow: 2px 3px 8px rgba(0,0,0,.35);
  }
  .tab { position: absolute; background: var(--tab-grey); }

  /* Letter */
  .letter { left: 75px; top: 72px; width: 684px; height: 971px; }
  .letter .tab-top { left: 410px; top: 0; width: 250px; height: 18px; }
  .letter .tab-bottom { left: 410px; bottom: 0; width: 250px; height: 16px; }
  .fold-mark { position: absolute; left: -12px; width: 18px; height: 1px; background: #888; }
  .wordmark { position: absolute; display: flex; align-items: center; gap: 8px; color: var(--brand-blue); font-weight: 600; letter-spacing: .5px; text-transform: uppercase; white-space: nowrap; }
  .wordmark .mark { width: 12px; height: 12px; background: var(--brand-blue); flex: none; }
  .letter .wordmark { left: 410px; top: 86px; font-size: 21px; }
  .sender-line { position: absolute; left: 78px; top: 166px; font-size: 7.5px; color: var(--brand-blue); letter-spacing: .3px; text-transform: uppercase; }
  .contact { position: absolute; font-size: 11.5px; line-height: 16px; color: var(--brand-blue); }
  .contact dl { display: grid; grid-template-columns: 48px auto; }
  .contact dt { font-weight: 700; }
  .letter .contact { left: 410px; top: 180px; }
  .letter .contact address { font-style: normal; margin-bottom: 16px; }
  .recipient { position: absolute; left: 78px; top: 222px; font-size: 11.5px; line-height: 16px; font-style: normal; }
  .date { position: absolute; left: 410px; top: 310px; font-size: 11.5px; }
  .letter-body { position: absolute; left: 78px; top: 344px; width: 532px; font-size: 10.2px; line-height: 15px; letter-spacing: -0.1px; }
  .subject { font-weight: 700; margin-bottom: 24px; }
  .salutation { margin-bottom: 13px; }
  .letter-body p.text { margin-bottom: 14px; }
  .closing { margin-top: 34px; }
  .closing .company { margin-top: 13px; }
  .signature { width: 62px; height: 22px; margin: 2px 0 3px; background: linear-gradient(90deg, #2a2a2a 0%, #555 100%); opacity: .18; border-radius: 3px; }
  .footer-line { position: absolute; left: 78px; top: 950px; font-size: 7.5px; color: var(--brand-blue); letter-spacing: .3px; text-transform: uppercase; }

  /* Business cards */
  .card { width: 444px; height: 255px; overflow: hidden; }
  .card-front { left: 708px; top: 300px; }
  .card-front .wordmark { left: 60px; top: 112px; font-size: 26px; }
  .card-back { left: 708px; top: 585px; }
  .card-back .tab-top { right: 0; top: 0; width: 177px; height: 18px; }
  .card-back .tab-bottom { right: 0; bottom: 0; width: 177px; height: 22px; }
  .card-title { position: absolute; right: 27px; top: 45px; text-align: right; color: var(--brand-blue); }
  .card-title .degree { font-size: 16px; line-height: 20px; }
  .card-title .name { font-size: 19px; font-weight: 700; line-height: 26px; }
  .card-title .role { font-size: 11px; line-height: 14px; }
  .card-back .contact { left: 30px; top: 132px; font-size: 12.5px; line-height: 16px; }
  .card-back .contact address { font-style: normal; margin-bottom: 16px; }
  .card-back .contact dl { grid-template-columns: 60px auto; }

  .caption { position: absolute; left: 78px; top: 1080px; font-size: 22px; font-weight: 700; color: var(--caption); }
</style>
</head>
<body>
<main class="stage">

  <article class="sheet letter">
    <div class="tab tab-top"></div>
    <div class="tab tab-bottom"></div>
    <span class="fold-mark" style="top:345px"></span>
    <span class="fold-mark" style="top:483px"></span>

    <div class="wordmark"><span class="mark"></span>Holger Varnbeck</div>
    <div class="sender-line">Holger Varnbeck &nbsp;|&nbsp; Musterstr. 123 &nbsp;|&nbsp; 01234 Musterstadt</div>

    <div class="contact">
      <address>Musterstr. 123<br>01234 Musterstadt</address>
      <dl>
        <dt>PHONE:</dt><dd>+41 41 7250416</dd>
        <dt>MAIL:</dt><dd>kontakt@kanzlei-varnbeck.de</dd>
        <dt>WEB:</dt><dd>www.kanzlei-varnbeck.de</dd>
      </dl>
    </div>

    <address class="recipient">Frau<br>Maria Mustermann<br>Feldstraße 1<br>11111 Musterstadt</address>
    <div class="date">Musterstadt, 17. Februar 2011</div>

    <div class="letter-body">
      <p class="subject">Betreffzeile</p>
      <p class="salutation">Sehr geehrte Frau Mustermann,</p>
      <p class="text">dies ist ein Typoblindtext. An ihm kann man sehen, ob alle Buchstaben da sind und wie sie aussehen. Manchmal benutzt man Worte wie Hamburgefonts, Rafgenduks oder Handgloves, um Schriften zu testen. Manchmal Sätze, die alle Buchstaben des Alphabets enthalten – man nennt diese Sätze »Pangrams«. Sehr bekannt ist dieser: The quick brown fox jumps over the lazy old dog. Oft werden in Typoblindtexte auch fremdsprachige Satzteile eingebaut (AVAIL® and Wefox™ are testing aussi la Kerning), um die Wirkung in anderen Sprachen zu testen. In Lateinisch sieht zum Beispiel fast jede Schrift gut aus. Quod erat demonstrandum. Seit 1975 fehlen in den meisten Testtexten die Zahlen, weswegen nach TypoGb. 204 § ab dem Jahr 2034 Zahlen in 86 der Texte zur Pflicht werden. Nichteinhaltung wird mit bis zu 245 € oder 368 $ bestraft.</p>
      <p class="text">Genauso wichtig in sind mittlerweile auch Âçcèñtë, die in neueren Schriften aber fast immer enthalten sind. Ein wichtiges aber schwierig zu integrierendes Feld sind OpenType-Funktionalitäten. Je nach Software und Voreinstellungen können eingebaute Kapitälchen, Kerning oder Ligaturen (sehr pfiffig) nicht richtig dargestellt werden. Dies ist ein Typoblindtext. An ihm kann man sehen, ob alle Buchstaben da sind und wie sie aussehen. Manchmal benutzt man Worte wie Hamburgefonts, Rafgenduks oder Handgloves, um Schriften zu testen. Manchmal Sätze, die alle Buchstaben des Alphabets enthalten – man nennt diese Sätze »Pangrams«.</p>
      <p class="text">Seit 1975 fehlen in den meisten Testtexten die Zahlen, weswegen nach TypoGb. 204 § ab dem Jahr 2034 Zahlen in 86 der Texte zur Pflicht werden. Nichteinhaltung wird mit bis zu 245 € oder 368 $ bestraft. Genauso wichtig in sind mittlerweile auch Âçcèñtë, die in neueren Schriften aber fast immer enthalten sind. Ein wichtiges aber schwierig zu integrierendes Feld sind OpenType-Funktionalitäten. Je nach Software und Voreinstellungen können eingebaute Kapitälchen, Kerning oder Ligaturen (sehr pfiffig) nicht richtig dargestellt werden.</p>

      <div class="closing">
        <p>Mit freundlichen Grüßen</p>
        <p class="company">Firma Mustermann</p>
        <div class="signature" role="img" aria-label="Handschriftliche Unterschrift"></div>
        <p>Max Mustermann</p>
      </div>
    </div>

    <div class="footer-line">Bank Musterstadt &nbsp;|&nbsp; BLZ 123 456 78 &nbsp;|&nbsp; Konto 0 123 456 789</div>
  </article>

  <section class="sheet card card-front" aria-label="Visitenkarte Vorderseite">
    <div class="wordmark"><span class="mark"></span>Holger Varnbeck</div>
  </section>

  <section class="sheet card card-back" aria-label="Visitenkarte Rückseite">
    <div class="tab tab-top"></div>
    <div class="tab tab-bottom"></div>
    <div class="card-title">
      <div class="degree">Dipl. Kaufmann</div>
      <div class="name">Holger Varnbeck</div>
      <div class="role">Steuerberater</div>
    </div>
    <div class="contact">
      <address>Musterstr. 123<br>01234 Musterstadt</address>
      <dl>
        <dt>PHONE:</dt><dd>+41 41 7250416</dd>
        <dt>MAIL:</dt><dd>kontakt@kanzlei-varnbeck.de</dd>
        <dt>WEB:</dt><dd>www.kanzlei-varnbeck.de</dd>
      </dl>
    </div>
  </section>

  <p class="caption">Geschäftsbrief nach DIN 676b</p>
</main>
</body>
</html>
```